Flyer Design

I need a flyer as Iam starting a business which cleans Leather couches,sofas,chairs for residential and businesses.
We clean the interiors of automobiles and marine craft, boats large and small.
We would like to be able to get across the message that we are affordable, personal and reliable.
The Gold coast is our market and within this area there is a large amount of holiday apartments and houses which do experience high traffic to their living and dinning areas.

Target Market(s)

Target market Home,Apartment,Marine and Auto Owners

Industry/Entity Type

Residential

Requirements
Must have
• The flyer must have Company name which is BRIGHT HIDE CARE MOBILE NUMBER
0471932054
EMAIL marvtolk@quellnet.com
Colours would like bright Gold or green or Red eith black lettering very modern font
Nice to have
• I would like to keep it as simple and clean looking.but eye catching
Should not have
• Dont want the flyer to look like a Real Estate flyer or a pizza advertisement.

```html
<!DOCTYPE html>
<html lang="en">
<head>
<meta charset="utf-8">
<title>Bright Hide Care – Flyer</title>
<link rel="stylesheet" href="https://fonts.googleapis.com/css2?family=Exo+2:wght@200;400;500;700;800&display=swap">
<style>
  :root {
    --red: #d0202a;
    --ink: #111111;
    --paper: #ffffff;
    --paper-shade: #f1f1f1;
    --band: #0d0d0d;
    --white: #ffffff;
  }
  * { margin: 0; padding: 0; box-sizing: border-box; }
  html, body { width: 933px; height: 1200px; overflow: hidden; background: #e6e6e6; }
  .flyer {
    position: relative; width: 933px; height: 1200px; overflow: hidden;
    background: linear-gradient(180deg, var(--paper) 0%, var(--paper-shade) 100%);
    font-family: "Exo 2", sans-serif; color: var(--ink);
  }
  .brand-title { position: absolute; left: 44px; top: 30px; line-height: 82px; font-size: 98px; letter-spacing: -1px; }
  .brand-title span { display: block; }
  .brand-strong { color: var(--red); font-weight: 700; }
  .brand-light { color: var(--ink); font-weight: 200; }
  .rule { position: absolute; left: 48px; width: 438px; height: 3px; background: var(--red); }
  .rule-top { top: 314px; }
  .rule-bottom { top: 860px; }
  .tagline {
    position: absolute; left: 46px; top: 330px;
    font-weight: 800; font-size: 58px; line-height: 55px; letter-spacing: -0.5px;
  }
  .services-heading {
    position: absolute; left: 48px; top: 546px;
    color: var(--red); font-weight: 400; font-size: 27px;
  }
  .services-list { position: absolute; left: 48px; top: 594px; list-style: none; font-weight: 500; font-size: 27px; line-height: 26px; }
  .services-list li { margin-bottom: 26px; }
  .cta {
    position: absolute; left: 48px; top: 890px;
    font-weight: 800; font-size: 35px; line-height: 32px;
  }
  .photo {
    position: absolute; left: 557px; top: 0; width: 329px; height: 1020px;
    background: linear-gradient(180deg, #ecebe6 0%, #ddd9d2 25%, #3a2b25 32%, #2a1d18 60%, #3b2a23 78%, #d8d4cd 86%, #8a6a55 95%, #b69a80 100%);
  }
  .band-line { position: absolute; left: 0; top: 1020px; width: 933px; height: 8px; background: var(--red); }
  .band { position: absolute; left: 0; top: 1028px; width: 933px; height: 172px; background: var(--band); }
  .band-brand { position: absolute; left: 46px; top: 20px; font-size: 50px; line-height: 42px; }
  .band-brand span { display: block; }
  .band-brand .brand-light { color: var(--white); }
  .contact-icon { position: absolute; left: 436px; width: 58px; height: 58px; }
  .icon-phone { top: 24px; }
  .icon-mail { top: 92px; }
  .phone {
    position: absolute; right: 46px; top: 20px;
    color: var(--white); font-weight: 400; font-size: 56px; letter-spacing: 1px;
  }
  .email {
    position: absolute; right: 46px; top: 86px; text-align: right;
    color: var(--white); font-weight: 500; font-size: 26px; line-height: 28px;
  }
</style>
</head>
<body>
<div class="flyer">
  <h1 class="brand-title">
    <span class="brand-strong">BRIGHT</span>
    <span class="brand-strong">HIDE</span>
    <span class="brand-light">CARE</span>
  </h1>
  <div class="rule rule-top"></div>
  <p class="tagline">AFFORDABLE,<br>PERSONAL,<br>RELIABLE!</p>
  <p class="services-heading">CLEANING SERVICES INCLUDE -</p>
  <ul class="services-list">
    <li>LEATHER SOFAS, COUCHES<br>&amp; CHAIRS</li>
    <li>DOMESTIC &amp; COMMERCIAL</li>
    <li>AUTOMOBILE &amp; MARINECRAFT<br>INTERIOR - SMALL &amp; LARGE</li>
    <li>+ MORE!</li>
  </ul>
  <div class="rule rule-bottom"></div>
  <p class="cta">CONTACT US FOR MORE<br>INFORMATION...</p>

  <div class="photo" role="img" aria-label="Dark brown leather sofa in a bright living room with a shaggy rug"></div>

  <div class="band-line"></div>
  <footer class="band">
    <div class="band-brand">
      <span class="brand-strong">BRIGHT</span>
      <span class="brand-strong">HIDE</span>
      <span class="brand-light">CARE</span>
    </div>
    <svg class="contact-icon icon-phone" viewBox="0 0 58 58" aria-hidden="true">
      <circle cx="29" cy="29" r="25" fill="none" stroke="#fff" stroke-width="4"/>
      <path d="M20 15c2-1 4-1 5 1l3 6c1 2 0 3-1 4l-2 2c1 4 4 7 8 9l2-2c1-1 2-2 4-1l6 3c2 1 2 3 1 5l-2 3c-2 2-5 2-8 1-9-4-15-10-19-19-1-3-1-6 1-8z" fill="#fff"/>
    </svg>
    <svg class="contact-icon icon-mail" viewBox="0 0 58 58" aria-hidden="true">
      <text x="29" y="45" text-anchor="middle" font-family="Exo 2, sans-serif" font-size="56" font-weight="500" fill="#fff">@</text>
    </svg>
    <p class="phone">0471932054</p>
    <p class="email">marvtolk@<br>quellnet.com</p>
  </footer>
</div>
</body>
</html>
```